Brightmoor Capital
"The Business and Corporate Finance Specialists, Mortgages and Remortgages"
Professional
Dorian Kellaway
Director
14 Quillfield Parade
Harrow
London
HA7 2QX
Dorian@brightmoorcapital.example
www.brightmoorcapital.example
Letterhead and compliment slips require the following regulatory text:
"Registered in England and Wales number: 08213947
Brightmoor Capital Ltd is authorised and regulated by the Monetary Oversight Council for regulated mortgage contracts and non-investment insurance activities."
Be creative - open to suggestions

```html
<!DOCTYPE html>
<html lang="en">
<head>
<meta charset="utf-8">
<title>Brightmoor Capital – Business Card</title>
<link href="https://fonts.googleapis.com/css2?family=Didact+Gothic&display=swap" rel="stylesheet">
<style>
  :root {
    --canvas-bg: #e9e7e3;
    --card-dark: #0c0c0c;
    --card-light: #ffffff;
    --brand-green: #8cc63f;
    --brand-orange: #f07a1a;
    --ink: #3a3a3a;
    --ink-soft: #7a7a7a;
    --on-dark: #e6e6e6;
    --on-dark-soft: #9a9a9a;
  }
  * { margin: 0; padding: 0; box-sizing: border-box; }
  html, body { width: 1200px; height: 646px; overflow: hidden; }
  body {
    background: var(--canvas-bg);
    font-family: "Didact Gothic", "Century Gothic", sans-serif;
    display: flex;
    align-items: center;
    justify-content: center;
    gap: 40px;
  }
  .card {
    width: 520px;
    height: 298px;
    position: relative;
    overflow: hidden;
    box-shadow: 0 6px 18px rgba(0,0,0,.18);
  }

  /* Back of card */
  .card--back {
    background: radial-gradient(ellipse at 40% 60%, #1c1c1c 0%, var(--card-dark) 70%);
    color: var(--on-dark);
  }
  .back-brand {
    position: absolute;
    left: 0; right: 0; top: 104px;
    text-align: center;
  }
  .brand-name {
    font-size: 40px;
    letter-spacing: .5px;
    line-height: 1;
  }
  .card--back .brand-name { color: var(--brand-green); }
  .back-tagline {
    margin-top: 10px;
    font-size: 11px;
    line-height: 1.45;
    color: var(--on-dark-soft);
    letter-spacing: .3px;
  }
  .back-web {
    position: absolute;
    left: 0; right: 0; bottom: 26px;
    text-align: center;
    font-size: 11px;
    color: var(--on-dark-soft);
    letter-spacing: .6px;
  }

  /* Front of card */
  .card--front {
    background: var(--card-light);
    color: var(--ink);
  }
  .front-wash {
    position: absolute;
    left: -40px; bottom: -60px;
    width: 300px; height: 220px;
    background: radial-gradient(ellipse at center, rgba(140,198,63,.12) 0%, rgba(240,122,26,.06) 45%, rgba(255,255,255,0) 72%);
  }
  .front-brand {
    position: absolute;
    left: 36px; top: 30px;
  }
  .card--front .brand-name {
    font-size: 30px;
    color: var(--brand-green);
  }
  .front-tagline {
    margin-top: 6px;
    font-size: 9px;
    line-height: 1.4;
    color: var(--ink-soft);
  }
  .contact {
    position: absolute;
    right: 32px; top: 112px;
    text-align: right;
  }
  .contact-name {
    font-size: 15px;
    color: var(--brand-orange);
    margin-bottom: 10px;
  }
  .contact-role { color: var(--ink); }
  .contact-divider { color: var(--ink-soft); margin: 0 4px; }
  .contact-list { list-style: none; font-size: 11px; line-height: 1.9; }
  .contact-list li {
    display: flex;
    justify-content: flex-end;
    align-items: center;
    gap: 8px;
  }
  .contact-list .address { line-height: 1.4; margin-bottom: 4px; display: block; }
  .icon {
    width: 13px; height: 13px;
    flex: none;
  }
</style>
</head>
<body>

  <section class="card card--back" aria-label="Business card, back">
    <div class="back-brand">
      <div class="brand-name">Brightmoor Capital</div>
      <p class="back-tagline">The Business and Corporate Finance Specialists<br>Mortgages and Remortgages</p>
    </div>
    <p class="back-web">www.brightmoorcapital.example</p>
  </section>

  <section class="card card--front" aria-label="Business card, front">
    <div class="front-wash"></div>
    <div class="front-brand">
      <div class="brand-name">Brightmoor Capital</div>
      <p class="front-tagline">The Business and Corporate Finance Specialists<br>Mortgages and Remortgages</p>
    </div>

    <div class="contact">
      <p class="contact-name">Dorian Kellaway<span class="contact-divider">/</span><span class="contact-role">Director</span></p>
      <ul class="contact-list">
        <li class="address">14 Quillfield Parade<br>Harrow, London HA7 2QX</li>
        <li>+44 (0)20 8123 4567
          <svg class="icon" viewBox="0 0 16 16" aria-hidden="true"><circle cx="8" cy="8" r="8" fill="var(--brand-orange)"/><path d="M5.2 4.2l1.4-.3.8 2-1 .7c.5 1.1 1.3 1.9 2.4 2.4l.7-1 2 .8-.3 1.4c-3.4.2-6.2-2.6-6-6z" fill="#fff"/></svg></li>
        <li>+44 (0)7700 900 123
          <svg class="icon" viewBox="0 0 16 16" aria-hidden="true"><circle cx="8" cy="8" r="8" fill="var(--brand-orange)"/><rect x="5.6" y="3.6" width="4.8" height="8.8" rx="1" fill="#fff"/><rect x="6.4" y="4.8" width="3.2" height="5.2" fill="var(--brand-orange)"/></svg></li>
        <li>+44 (0)20 8123 4568
          <svg class="icon" viewBox="0 0 16 16" aria-hidden="true"><circle cx="8" cy="8" r="8" fill="var(--brand-orange)"/><rect x="4" y="6.5" width="8" height="5" rx="1" fill="#fff"/><rect x="5.5" y="4" width="5" height="3" fill="#fff"/></svg></li>
        <li>Dorian@brightmoorcapital.example
          <svg class="icon" viewBox="0 0 16 16" aria-hidden="true"><circle cx="8" cy="8" r="8" fill="var(--brand-orange)"/><rect x="4" y="5" width="8" height="6" fill="#fff"/><path d="M4 5l4 3.4L12 5" fill="none" stroke="var(--brand-orange)" stroke-width="1"/></svg></li>
        <li>www.brightmoorcapital.example
          <svg class="icon" viewBox="0 0 16 16" aria-hidden="true"><circle cx="8" cy="8" r="8" fill="var(--brand-orange)"/><circle cx="8" cy="8" r="4" fill="none" stroke="#fff" stroke-width="1"/><path d="M4 8h8M8 4c-1.6 2.4-1.6 5.6 0 8M8 4c1.6 2.4 1.6 5.6 0 8" fill="none" stroke="#fff" stroke-width=".8"/></svg></li>
      </ul>
    </div>
  </section>

</body>
</html>
```